Help us Create Excitement with a Food To Go Web Site Menu

We are seeking a design that can serve as a template for a Wordpress based website. The template will present the name (BrimBowl), present the menu items with price details, and contact details. The final design should NOT have the Mingle Kerb Eats subtitle anywhere in the site.
Our plan is to have the menu with basic graphic elements with the options to link to images/pictures of the menu item (perhaps linked via Instagram or something like that if possible).
Updates

Target Market(s)

Home dining menu intended to offer perspective customers an understanding of what they will be enjoying.

Contact Information for Business Card

BrimBowl logo (without the Mingle Kerb Eats tag line included)
hi@brimbowl.com.au
Phone: XXXX XXX XXX (to be provided)

Coding

Coded - Design and coding required

Number of Pages Required

2 page

Requirements
Must have
• A bold and colourful presence that is also on the playful side.

A clearly readable menu layout that doesn't feel small based on the limited number of items that we offer at this time.
Nice to have
• A playful semi-graffiti based feel would be nice to convey a sense of playfulness.
Should not have
• The design should not have an overly Asian feel to it.

It appears many people are misreading the brief so I am adding this point to clarify one of the design requirements.
-- The final design should NOT have the Mingle Kerb Eats subtitle anywhere in the site, including the logo.

```html
<!DOCTYPE html>
<html lang="en">
<head>
<meta charset="utf-8">
<title>BrimBowl – Menu</title>
<link rel="stylesheet" href="https://fonts.googleapis.com/css2?family=Oswald:wght@400;500&family=Poppins:wght@400;500;600;700&family=Roboto+Condensed:wght@400;700&family=Lato:wght@400&display=swap">
<style>
:root{
  --red:#ff0000;
  --red-deep:#e00000;
  --maroon:#7a0000;
  --ink:#000;
  --text:#555;
  --muted:#888;
  --hero-bg:#f7f7f7;
  --white:#fff;
}
*{margin:0;padding:0;box-sizing:border-box}
html,body{width:850px;height:1200px;overflow:hidden;background:var(--white)}
body{position:relative;font-family:'Lato',sans-serif;color:var(--ink)}
.hero{position:absolute;left:0;top:0;width:850px;height:478px;background:var(--hero-bg);overflow:hidden}
.hero-shape{position:absolute;left:0;top:0}
.brand{position:absolute;left:117px;top:28px;display:flex;align-items:center;gap:7px;font-family:'Poppins',sans-serif;font-weight:700;font-size:24px;color:var(--red-deep)}
.brand-dot{width:14px;height:14px;border-radius:50%;background:var(--ink)}
.call{position:absolute;left:589px;top:21px;display:flex;gap:7px}
.call-label{font-family:'Poppins',sans-serif;font-size:8.5px;color:var(--red-deep);display:block}
.call-number{font-family:'Roboto Condensed',sans-serif;font-weight:700;font-size:12px;color:var(--maroon);display:block;margin-top:3px}
.menu-toggle{position:absolute;left:697px;top:21px;width:27px;height:27px;border-radius:50%;background:var(--maroon);display:flex;flex-direction:column;justify-content:center;align-items:center;gap:2.5px}
.menu-toggle span{width:12px;height:2px;background:var(--white);border-radius:1px}
.hero-title{position:absolute;left:115px;top:165px;font-family:'Oswald',sans-serif;font-weight:500;font-size:33px;line-height:40px;letter-spacing:-0.8px;color:var(--ink)}
.hero-title em{font-style:normal;color:var(--red)}
.hero-copy{position:absolute;left:115px;top:295px;width:245px;font-size:8.5px;line-height:16px;color:var(--text)}
.btn{position:absolute;display:flex;align-items:center;justify-content:center;background:var(--maroon);color:var(--white);font-family:'Poppins',sans-serif;font-size:9.5px;height:32px}
.hero-btn{left:114px;top:341px;width:85px}
.bowl{position:absolute;left:471px;top:120px;width:292px;height:292px;border-radius:50%;background:radial-gradient(circle,#7ba84a 0%,#9c8a5a 50%,#d9d2c4 72%,#f1f1f1 76%,#e9e9e9 100%)}
.section-title{position:absolute;left:0;width:850px;text-align:center;font-family:'Poppins',sans-serif;font-weight:600;font-size:22px;color:var(--ink)}
.dishes-title{top:515px}
.dish-panel{position:absolute;left:138px;top:569px;width:574px;height:347px;background:var(--ink);border-radius:6px;overflow:hidden}
.tabs{display:flex;height:48px}
.tab{flex:1;display:flex;align-items:center;justify-content:center;text-align:center;padding:0 8px;background:var(--red);color:var(--white);font-family:'Roboto Condensed',sans-serif;font-size:11px;line-height:16px;border-left:1px solid var(--white)}
.tab.is-active{background:var(--ink);border-left:none}
.dish-photo{position:absolute;left:37px;top:89px;width:214px;height:214px;border-radius:50%;border:1px solid var(--red);background:radial-gradient(circle at 45% 45%,#f1e6d6 0%,#e8c9a4 55%,#c69a6b 85%,#4a3a32 100%)}
.dish-name{position:absolute;left:304px;top:113px;font-family:'Poppins',sans-serif;font-weight:600;font-size:16px;color:var(--red)}
.dish-copy{position:absolute;left:304px;top:143px;width:230px;font-size:7px;line-height:13.8px;color:var(--white)}
.dish-btn{left:303px;top:247px;width:95px}
.news-title{top:953px}
.news-copy{position:absolute;left:0;top:996px;width:850px;text-align:center;font-size:8.5px;line-height:16px;color:var(--muted)}
.email{position:absolute;left:252px;top:1041px;width:345px;height:32px;border:1px solid #ccc;background:#fafafa;padding-left:9px;display:flex;align-items:center;font-size:7px;color:var(--text)}
.news-btn{left:377px;top:1079px;width:95px}
.footer{position:absolute;left:0;top:1152px;width:850px;height:48px;background:var(--red-deep);display:flex;align-items:center;justify-content:center;font-size:7.5px;color:var(--white)}
</style>
</head>
<body>
<header class="hero">
  <svg class="hero-shape" width="850" height="478" viewBox="0 0 850 478">
    <path d="M756 0 H850 V145 C800 150 778 185 778 240 L778 264 C778 354 705 426 616 426 C527 426 454 354 454 264 C454 174 527 100 616 100 C650 100 675 98 695 85 C730 60 735 25 742 10 C745 4 750 0 756 0 Z" fill="#ee0000"/>
  </svg>
  <div class="bowl" role="img" aria-label="Bowl of beef noodle soup with fresh herbs, seen from above"></div>
  <div class="brand"><span class="brand-dot"></span>BrimBowl</div>
  <div class="call">
    <svg width="20" height="27" viewBox="0 0 20 27"><path d="M4 1 L8 1 L9 8 L6 10 C7 15 10 19 14 21 L16 18 L20 21 L18 26 C9 26 1 16 1 5 Z" fill="#e00000"/></svg>
    <div><span class="call-label">Call Us Now</span><span class="call-number">555.010.2468</span></div>
  </div>
  <div class="menu-toggle"><span></span><span></span><span></span></div>
  <h1 class="hero-title">Your Favourite<br><em>Food Delivered Hot<br>&amp; Fresh</em></h1>
  <p class="hero-copy">Lorem ipsum dolor sit amet, consectetur adipiscing elit, sed do eiusmod tempor incididunt ut labore et dolore magna aliqua.</p>
  <a class="btn hero-btn">ORDER NOW</a>
</header>

<h2 class="section-title dishes-title">Our Delicious Dish</h2>
<section class="dish-panel">
  <div class="tabs">
    <div class="tab is-active">Ph (beef noodle<br>soup) $14</div>
    <div class="tab">Egg Rolls (life changing)<br>$10 for 10</div>
    <div class="tab">Crab Soup (mmm so good, so fresh) &nbsp;$ Market Price</div>
    <div class="tab">Tuna Salad Sandwich (sweet, sour, and tangy) $9</div>
  </div>
  <div class="dish-photo" role="img" aria-label="Spoonful of creamy crab and corn soup"></div>
  <h3 class="dish-name">Ph (beef noodle soup) $14</h3>
  <p class="dish-copy">Just like Ba (Grandma) used to make. Our Pho takes 12 hours to make. We boil and reduce our own broth, using the freshest, locally sourced ingredients. We use real beef filet, brisket, and Vietnamese meatballs paired with crispy beansprouts, green onion, cilantro, and Asian basil. We provide Hoisin and Sriracha (hot sauce) to create your perfect fusion of flavours.</p>
  <a class="btn dish-btn">ADD TO ORDER</a>
</section>

<h2 class="section-title news-title">Subcribe Newsletter</h2>
<p class="news-copy">Lorem ipsum dolor sit amet, consectetur adipiscing elit, sed do eiusmod<br>tempor incididunt magna aliqua.</p>
<div class="email">Enter Email.....</div>
<a class="btn news-btn">SUBCRIBE NOW</a>

<footer class="footer">Copyright © BRIMBOWL - 2020 . All Right Reserved.</footer>
</body>
</html>
```